Word Document Estimate Sheet

Good evening. I have an home renovations company that does a lot of estimates through word documents and then emailed them a PDF document. ArtHarbor did my logo and stationary projects and did a great job with it. Now I need my word document estimate sheet to be more standardized meaning sometimes my headers and footers move when I get to the bottom of the page , this make me have to do a copy and paste many times to put them back in their place also I have headings like Master Bedroom, Master Bath . I would like for them to always be bold, underlined and colon on the end now I always have to do this. I would like for the header and footers to not move when I get to the bottom of the page. Basically I want the same document with the same look as the document I send but with less retyping and copy and pasting. Hopefully this makes sense and you can help my estimates go faster.

Thanks,
Glen

Target Market(s)

Customer who want an estimate

Industry/Entity Type

It Company

Requirements
Must have
• 1.Must have same header and footer as the document I sent but want text to be standard.
• 2.Header and footer must not move when I get to the bottom of page.
• 3.Categories like Master Bedroom, Kitchen Area categories must already be in the document and if I want to delete them I can.
Nice to have
• I would love my estimate time to be cut in half because new word estimate sheet is simple to work with.
Should not have
• Don't change the header and footer design at all just make sure it doesn't move when I type.

```html
<!DOCTYPE html>
<html lang="en">
<head>
<meta charset="utf-8">
<title>Estimate Sheet – Harlow Home Renovations</title>
<link href="https://fonts.googleapis.com/css2?family=Tinos:wght@400;700&display=swap" rel="stylesheet">
<style>
  :root {
    --header-grey: #e1e1e1;
    --rule-navy: #1f3a5f;
    --footer-navy: #1a0f4c;
    --brand-navy: #231a5a;
    --heading-bar: #e2e2e2;
    --ink: #1e1e1e;
    --white: #ffffff;
  }
  * { margin: 0; padding: 0; box-sizing: border-box; }
  html, body { width: 848px; height: 1200px; overflow: hidden; background: var(--white); }
  body { position: relative; font-family: "Tinos", "Times New Roman", serif; color: var(--ink); }

  .page-header {
    position: absolute; top: 0; left: 0; width: 848px; height: 120px;
    background: var(--header-grey);
    display: flex; align-items: center; justify-content: center; gap: 10px;
  }
  .page-header::after {
    content: ""; position: absolute; left: 0; bottom: -8px; width: 100%; height: 8px;
    background: var(--rule-navy);
  }
  .brand-mark { width: 14px; height: 14px; background: var(--brand-navy); }
  .brand-name {
    font-weight: 700; font-size: 22px; letter-spacing: 1.5px; color: var(--brand-navy);
    text-transform: uppercase;
  }

  .estimate-section { position: absolute; left: 53px; width: 742px; }
  .section-title {
    height: 40px; background: var(--heading-bar);
    font-weight: 700; font-size: 24px; line-height: 42px; padding-left: 8px;
  }
  .scope-list { list-style: none; margin: 12px 0 0 65px; width: 652px; }
  .scope-list li {
    position: relative; font-size: 19.5px; line-height: 24px; margin-bottom: 10.5px;
    text-align: justify;
  }
  .scope-list li::before {
    content: ""; position: absolute; left: -22px; top: 9px;
    width: 6px; height: 6px; border-radius: 50%; background: var(--ink);
  }

  .laundry { top: 168px; }
  .hall-bath { top: 390px; }
  .master-bedroom { top: 646px; }
  .master-bath { top: 869px; }

  .page-footer {
    position: absolute; left: 0; bottom: 0; width: 848px; height: 114px;
    background: var(--footer-navy); color: var(--white);
    text-align: center; font-size: 13.5px; line-height: 20.5px; padding-top: 22px;
  }
  .footer-site { font-weight: 700; font-size: 14px; }
  .sep { margin: 0 6px; }
</style>
</head>
<body>
  <header class="page-header">
    <span class="brand-mark"></span>
    <span class="brand-name">Harlow Home Renovations</span>
  </header>

  <section class="estimate-section laundry">
    <h2 class="section-title">Washer &amp; Dryer Area:</h2>
    <ul class="scope-list">
      <li>Clean &amp; paint all base molding in stated area a semi-gloss white color</li>
      <li>Clean both doors in stated area first and if it’s determined it needs to be painted we will discuss with customer for pricing before painting it.</li>
      <li>Clean and paint 2.25 wide trim on both sides of door’s.</li>
    </ul>
  </section>

  <section class="estimate-section hall-bath">
    <h2 class="section-title">Hall Bath:</h2>
    <ul class="scope-list">
      <li>Clean &amp; paint all base molding in stated area a semi-gloss white color</li>
      <li>Clean and paint 2.25 wide trim on both sides of door a semi-gloss white.</li>
      <li>Remove, replace and paint broken quarter-round at the base of tub.</li>
      <li>Clean both doors in stated area first and if it’s determined it needs to be painted we will discuss with customer for pricing before painting it.</li>
    </ul>
  </section>

  <section class="estimate-section master-bedroom">
    <h2 class="section-title">Master Bedroom:</h2>
    <ul class="scope-list">
      <li>Clean &amp; paint all base molding in stated area a semi-gloss white color</li>
      <li>Clean and paint 2.25 wide trim on both sides of doors a semi-gloss white.</li>
      <li>Clean all three doors in stated area first and if it’s determined it needs to be painted we will discuss with customer for pricing before painting it.</li>
    </ul>
  </section>

  <section class="estimate-section master-bath">
    <h2 class="section-title">Master Bathroom:</h2>
    <ul class="scope-list">
      <li>Repair ceiling and wall in stated area then prime and paint entire bathroom.</li>
      <li>Clean &amp; paint all base molding in stated area a semi-gloss white color</li>
      <li>Clean and paint door case molding on all 3 sides a semi-gloss white.</li>
      <li>Clean door in stated area first and if it’s determined it needs to be painted we will discuss with customer for pricing before painting it.</li>
    </ul>
  </section>

  <footer class="page-footer">
    <div class="footer-site">www.harlowhomereno.com</div>
    <div>Dana Harlow Office : 555-204-1187<span class="sep">|</span>Glen Harlow Cell : 555-204-1188<span class="sep">|</span>E-Mail: glen@harlowhomereno.com</div>
    <div>412 East Maple St., Suite 220 Riverton, NC 28000</div>
  </footer>
</body>
</html>
```